Business Card Design

We need a business card design for a new company based in Melbourne Australia. We are financial broker in finance industry. We provide a wide range of finance solutions to our clients including home loans, commercial loans, business facilities, car loans, equipment loans, invoice finance, etc. The company name is from director's personal name. We would like to have a new company logo that includes TK.

Industry/Entity Type

Business

Contact Information for Business Card

company name: TK & Co Finance Pty Ltd
person's name: Desmond Okafor
role: Managing Director
Mobile: 0417 638 294
fax: 03 9561 4472
Email: desmond.okafor@tkcolending.example
Address: Suite 5/418 Marlow Avenue Elmvale Vic 3174
Credit Licence No.: 718249

```html
<!DOCTYPE html>
<html lang="en">
<head>
<meta charset="utf-8">
<title>TK &amp; Co Finance Pty Ltd – Business Card</title>
<link rel="stylesheet" href="https://fonts.googleapis.com/css2?family=Source+Sans+3:wght@400;600&display=swap">
<style>
  :root {
    --stage-top: #262626;
    --stage-bottom: #070707;
    --card: #ffffff;
    --green: #76a83a;
    --orange: #f7921e;
    --grey: #7d7d7d;
  }
  * { margin: 0; padding: 0; box-sizing: border-box; }
  html, body { width: 1200px; height: 900px; overflow: hidden; }
  body {
    position: relative;
    background: linear-gradient(180deg, var(--stage-top) 0%, #1a1a1a 45%, var(--stage-bottom) 100%);
    font-family: "Source Sans 3", "Myriad Pro", Arial, sans-serif;
  }
  .card {
    position: absolute;
    top: 307px;
    width: 439px;
    height: 270px;
    background: var(--card);
    border-radius: 12px;
    overflow: hidden;
  }
  .card--front { left: 149px; }
  .card--back { left: 609px; }

  /* front: brand mark area */
  .brand-mark {
    position: absolute;
    left: 30px; top: 48px;
    width: 170px; height: 174px;
    display: flex; flex-direction: column;
    align-items: center; justify-content: center;
    gap: 14px;
  }
  .brand-mark__dot {
    width: 46px; height: 46px; border-radius: 50%;
    background: var(--orange);
  }
  .brand-mark__name {
    font-size: 30px; font-weight: 600; color: var(--orange);
    letter-spacing: 0.5px; white-space: nowrap;
  }

  /* front: contact block */
  .contact { position: absolute; left: 218px; top: 44px; right: 10px; }
  .contact__name { font-size: 17px; font-weight: 600; line-height: 1.1; }
  .contact__first { color: var(--green); }
  .contact__last { color: var(--orange); }
  .contact__role { font-size: 12.5px; color: var(--orange); margin-top: 2px; }
  .contact__list { list-style: none; margin-top: 20px; }
  .contact__item {
    display: flex; align-items: center; gap: 6px;
    font-size: 12.5px; color: var(--orange); height: 18.5px;
    white-space: nowrap;
  }
  .contact__item--email { font-size: 11px; letter-spacing: -0.1px; }
  .contact__icon { width: 9px; height: 9px; fill: var(--green); flex: none; margin-left: 2px; }
  .contact__address { font-size: 12.5px; color: var(--orange); line-height: 15.5px; margin-top: 10px; }
  .contact__licence { font-size: 12.5px; color: var(--orange); margin-top: 14px; margin-left: 3px; }
  .contact__licence-label { color: var(--green); font-weight: 600; }

  /* back: wordmark */
  .wordmark {
    position: absolute; inset: 0;
    display: flex; flex-direction: column;
    align-items: center; justify-content: center;
    gap: 16px;
  }
  .wordmark__square { width: 30px; height: 30px; background: var(--orange); }
  .wordmark__name {
    font-weight: 400; color: var(--orange);
    text-align: center; line-height: 1.1;
  }
  .wordmark__line { display: block; }
  .wordmark__line--main { font-size: 42px; letter-spacing: 1px; }
  .wordmark__line--sub { font-size: 30px; }
</style>
</head>
<body>
  <section class="card card--front" aria-label="Business card front">
    <div class="brand-mark">
      <span class="brand-mark__dot"></span>
      <span class="brand-mark__name">TK &amp; Co</span>
    </div>
    <div class="contact">
      <p class="contact__name"><span class="contact__first">Desmond</span> <span class="contact__last">Okafor</span></p>
      <p class="contact__role">Managing Director</p>
      <ul class="contact__list">
        <li class="contact__item">
          <svg class="contact__icon" viewBox="0 0 10 10" aria-hidden="true"><path d="M2.2 0.5 L3.6 2.6 L2.7 3.5 C3.3 4.8 5.1 6.6 6.4 7.2 L7.4 6.3 L9.5 7.7 L8.6 9.4 C4.6 9.2 0.8 5.4 0.6 1.4 Z"/></svg>
          0417 638 294
        </li>
        <li class="contact__item">
          <svg class="contact__icon" viewBox="0 0 10 10" aria-hidden="true"><path d="M2 0.5 H7 V3 H9.5 V9.5 H0.5 V3 H2 Z M3 1.5 V3 H6 V1.5 Z M2 5 V6 H4 V5 Z M5.5 5 V6 H8 V5 Z M2 7 V8 H4 V7 Z M5.5 7 V8 H8 V7 Z" fill-rule="evenodd"/></svg>
          03 9561 4472
        </li>
        <li class="contact__item contact__item--email">
          <svg class="contact__icon" viewBox="0 0 10 10" aria-hidden="true"><path d="M0.5 2 H9.5 V8.5 H0.5 Z"/><path d="M1 2.4 L5 5.4 L9 2.4" stroke="#fff" stroke-width="0.8" fill="none"/></svg>
          desmond.okafor@tkcolending.example
        </li>
      </ul>
      <p class="contact__address">Suite 5/418 Marlow Avenue<br>Elmvale Vic 3174</p>
      <p class="contact__licence"><span class="contact__licence-label">Credit Licence No.:</span> 718249</p>
    </div>
  </section>

  <section class="card card--back" aria-label="Business card back">
    <div class="wordmark">
      <span class="wordmark__square"></span>
      <p class="wordmark__name">
        <span class="wordmark__line wordmark__line--main">TK &amp; Co</span>
        <span class="wordmark__line wordmark__line--sub">Finance Pty Ltd</span>
      </p>
    </div>
  </section>
</body>
</html>
```